KWI Business Card

Please create a creative design for a business card using the new theme from the Logo & website. This company's main focus is food manufacturing building construction. Please integrate the new logo attached.

Please use the following information for the demo card:

Korvel Walls, Inc.
Dana Whitcombe
dwhitcombe@korvelwalls.example
Cell: 312-555-0178
218 Larkmoor Ave
Brenwick, KS 60418

See pictures and more information on the website.

www.korvelwalls.example

```html
<!DOCTYPE html>
<html lang="en">
<head>
<meta charset="UTF-8">
<title>KWI Business Card</title>
<link rel="stylesheet" href="https://fonts.googleapis.com/css2?family=Hind:wght@500;600;700&family=Montserrat:wght@400;500;600&display=swap">
<style>
  :root {
    --page-bg: #e9e9e9;
    --card-stock: #cfcbc7;
    --brand-blue: #2f7fcf;
    --ink: #4a4a4a;
    --icon: #3b3b3b;
    --shadow: rgba(0,0,0,0.28);
  }
  * { margin: 0; padding: 0; box-sizing: border-box; }
  html, body {
    width: 1200px; height: 1050px; overflow: hidden;
    background: var(--page-bg);
  }
  .sheet { position: relative; width: 1200px; height: 1050px; }
  .card {
    position: absolute; left: 204px; width: 792px; height: 480px;
    background: var(--card-stock);
    box-shadow: 0 4px 14px var(--shadow);
    overflow: hidden;
  }
  .card--front { top: 30px; }
  .card--back  { top: 540px; }

  .holder-name {
    position: absolute; left: 37px; top: 96px;
    display: flex; align-items: center; gap: 10px;
    font-family: "Hind", sans-serif; font-weight: 600; font-size: 25px;
    color: var(--brand-blue); letter-spacing: -0.2px; text-transform: uppercase;
    white-space: nowrap;
  }
  .holder-name__rule { width: 220px; height: 2px; background: var(--brand-blue); }

  .contact-list {
    position: absolute; left: 37px; top: 143px; list-style: none;
    font-family: "Montserrat", sans-serif; font-weight: 400; font-size: 20px; color: var(--ink);
  }
  .contact-list li { display: flex; align-items: center; height: 39px; white-space: nowrap; }
  .contact-list svg { width: 28px; height: 28px; margin-right: 14px; flex: none; }
  .contact-list .accent { color: var(--brand-blue); }

  .company {
    position: absolute; left: 30px; top: 338px;
    font-family: "Hind", sans-serif; font-weight: 700; font-size: 37px;
    color: var(--brand-blue); letter-spacing: -0.3px; text-transform: uppercase;
    white-space: nowrap;
  }
  .address {
    position: absolute; left: 35px; top: 385px;
    font-family: "Montserrat", sans-serif; font-size: 20px; line-height: 30px; color: var(--ink);
  }

  .brand-name {
    position: absolute; display: flex; align-items: center; gap: 10px;
    font-family: "Hind", sans-serif; font-weight: 700; color: var(--brand-blue);
    white-space: nowrap;
  }
  .brand-name__dot { border-radius: 50%; background: var(--brand-blue); flex: none; }
  .card--front .brand-name { left: 472px; top: 226px; font-size: 27px; }
  .card--front .brand-name__dot { width: 11px; height: 11px; }
  .card--back .brand-name {
    left: 0; right: 0; top: 212px; justify-content: center; font-size: 46px;
  }
  .card--back .brand-name__dot { width: 16px; height: 16px; }
</style>
</head>
<body>
<main class="sheet">
  <section class="card card--front">
    <div class="holder-name">Dana Whitcombe <span class="holder-name__rule"></span></div>
    <ul class="contact-list">
      <li>
        <svg viewBox="0 0 28 28" fill="none" stroke="var(--brand-blue)" stroke-width="1.8">
          <rect x="8" y="2" width="12" height="24" rx="2"/>
          <rect x="10.5" y="5" width="7" height="6"/>
          <path d="M11 15h2M15 15h2M11 18h2M15 18h2M11 21h2M15 21h2"/>
        </svg>
        312-555-0178
      </li>
      <li>
        <svg viewBox="0 0 28 28" fill="none" stroke="var(--icon)" stroke-width="1.8">
          <rect x="3" y="7" width="22" height="15"/>
          <path d="M3 7l11 9 11-9M3 22l8-7M25 22l-8-7"/>
        </svg>
        <span><span class="accent">dwhitcombe</span>@korvelwalls.example</span>
      </li>
      <li>
        <svg viewBox="0 0 28 28">
          <circle cx="14" cy="14" r="11" fill="var(--brand-blue)"/>
          <g fill="none" stroke="var(--card-stock)" stroke-width="1.3">
            <ellipse cx="14" cy="14" rx="5" ry="11"/>
            <path d="M3 14h22M5 8.5h18M5 19.5h18M14 3v22"/>
          </g>
        </svg>
        www.korvelwalls.example
      </li>
    </ul>
    <h1 class="company">Korvel Walls, Inc.</h1>
    <p class="address">218 Larkmoor Ave<br>Brenwick, KS 60418</p>
    <div class="brand-name"><span class="brand-name__dot"></span>Korvel Walls, Inc.</div>
  </section>

  <section class="card card--back">
    <div class="brand-name"><span class="brand-name__dot"></span>Korvel Walls, Inc.</div>
  </section>
</main>
</body>
</html>
```